Zielgruppe
Ich bin Coach und führe Gespräche mit Frauen die durch die Situation im Aussen oder Lebensümstände überlastet oder überfordert sind.
Aufgabenstellung
Ich mag ein klares und gleichzeitig liebevoll Frauen einladendes Design. Ich mag kein blau und grau dafür aber warme und natürliche Farben.
Ich brauche auch noch einen doppelseitigen Hochkantflyer
Der Text ist: Gespräche zu zweit - für Seelentrost und innere Harmonie (das ist die erste Idee)

```html
<!DOCTYPE html>
<html lang="de">
<head>
<meta charset="utf-8">
<title>Visitenkarte – Gespräche zu zweit</title>
<link rel="stylesheet" href="https://fonts.googleapis.com/css2?family=Libre+Franklin:wght@300;400;600;700&display=swap">
<style>
  :root {
    --page: #ffffff;
    --ink-light: #ffffff;
    --mauve: #d9c3d6;
    --sand: #ecdcc8;
    --sage: #c9dfc8;
    --rose: #f1b9c6;
    --peach: #f6cdb4;
    --apricot: #f3c29f;
    --butter: #f8ecaa;
    --mint: #bfe0cf;
  }
  html, body {
    margin: 0;
    padding: 0;
    width: 997px;
    height: 1200px;
    overflow: hidden;
    background: var(--page);
  }
  .sheet {
    position: relative;
    width: 997px;
    height: 1200px;
  }
  .card {
    position: absolute;
    left: 29px;
    width: 931px;
    display: block;
  }
  .card--front { top: 25px; height: 528px; }
  .card--back { top: 634px; height: 525px; }
  .tagline {
    font-family: "Libre Franklin", Arial, sans-serif;
    font-weight: 700;
    font-size: 27px;
    fill: var(--ink-light);
    letter-spacing: 0.3px;
  }
  .name {
    font-family: "Libre Franklin", Arial, sans-serif;
    font-weight: 700;
    font-size: 34px;
    fill: var(--ink-light);
  }
  .role {
    font-family: "Libre Franklin", Arial, sans-serif;
    font-weight: 700;
    font-size: 29px;
    fill: var(--ink-light);
  }
  .contact {
    font-family: "Libre Franklin", Arial, sans-serif;
    font-weight: 300;
    font-size: 22px;
    fill: var(--ink-light);
  }
</style>
</head>
<body>
<main class="sheet">

  <svg class="card card--front" viewBox="0 0 931 528" xmlns="http://www.w3.org/2000/svg">
    <defs>
      <linearGradient id="front-base" x1="0" y1="0" x2="1" y2="1">
        <stop offset="0" stop-color="#e6d6de"/>
        <stop offset="0.35" stop-color="var(--mauve)"/>
        <stop offset="0.7" stop-color="var(--sand)"/>
        <stop offset="1" stop-color="var(--mauve)"/>
      </linearGradient>
      <radialGradient id="front-sage-glow" cx="0.9" cy="0.15" r="0.45">
        <stop offset="0" stop-color="var(--sage)"/>
        <stop offset="1" stop-color="var(--sage)" stop-opacity="0"/>
      </radialGradient>
      <radialGradient id="front-sage-low" cx="0.1" cy="0.95" r="0.35">
        <stop offset="0" stop-color="var(--sage)"/>
        <stop offset="1" stop-color="var(--sage)" stop-opacity="0"/>
      </radialGradient>
      <radialGradient id="front-circle" cx="0.3" cy="0.3" r="0.9">
        <stop offset="0" stop-color="var(--rose)"/>
        <stop offset="0.4" stop-color="#eec3cf"/>
        <stop offset="0.7" stop-color="var(--peach)"/>
        <stop offset="1" stop-color="var(--mint)"/>
      </radialGradient>
      <radialGradient id="front-circle-butter" cx="0.45" cy="1" r="0.35">
        <stop offset="0" stop-color="var(--butter)"/>
        <stop offset="1" stop-color="var(--butter)" stop-opacity="0"/>
      </radialGradient>
      <clipPath id="front-clip"><rect width="931" height="528"/></clipPath>
    </defs>
    <g clip-path="url(#front-clip)">
      <rect class="front-base" width="931" height="528" fill="url(#front-base)"/>
      <rect width="931" height="528" fill="url(#front-sage-glow)"/>
      <rect width="931" height="528" fill="url(#front-sage-low)"/>
      <circle class="front-orb" cx="493" cy="262" r="317" fill="url(#front-circle)"/>
      <circle cx="493" cy="262" r="317" fill="url(#front-circle-butter)"/>
      <g transform="rotate(12 478 200)">
        <text class="tagline" x="478" y="190" text-anchor="middle">GESPRÄCHE ZU ZWEIT - FÜR SEELENTROST</text>
        <text class="tagline" x="468" y="224" text-anchor="middle">UND INNERE HARMONIE</text>
      </g>
    </g>
  </svg>

  <svg class="card card--back" viewBox="0 0 931 525" xmlns="http://www.w3.org/2000/svg">
    <defs>
      <linearGradient id="back-base" x1="0" y1="0" x2="1" y2="1">
        <stop offset="0" stop-color="var(--sage)"/>
        <stop offset="0.55" stop-color="var(--sand)"/>
        <stop offset="1" stop-color="var(--mauve)"/>
      </linearGradient>
      <radialGradient id="back-orb" cx="0.2" cy="0.2" r="0.95">
        <stop offset="0" stop-color="var(--rose)"/>
        <stop offset="0.4" stop-color="#eec3cf"/>
        <stop offset="0.7" stop-color="var(--apricot)"/>
        <stop offset="1" stop-color="var(--peach)"/>
      </radialGradient>
      <radialGradient id="back-orb-butter" cx="0.1" cy="0.85" r="0.35">
        <stop offset="0" stop-color="var(--butter)"/>
        <stop offset="1" stop-color="var(--butter)" stop-opacity="0"/>
      </radialGradient>
      <linearGradient id="dot-band-fade" x1="0" y1="0" x2="0" y2="1">
        <stop offset="0" stop-color="#ffffff" stop-opacity="0.16"/>
        <stop offset="1" stop-color="#ffffff" stop-opacity="0"/>
      </linearGradient>
      <clipPath id="back-clip"><rect width="931" height="525"/></clipPath>
    </defs>
    <g clip-path="url(#back-clip)">
      <rect width="931" height="525" fill="url(#back-base)"/>
      <rect class="dot-band" role="img" aria-label="Feines Punktraster als Zierband" x="0" y="0" width="931" height="110" fill="url(#dot-band-fade)"/>
      <circle class="back-orb" cx="164" cy="260" r="321" fill="url(#back-orb)"/>
      <circle cx="164" cy="260" r="321" fill="url(#back-orb-butter)"/>

      <text class="name" x="245" y="280" text-anchor="middle">Lotta Kirschbaum</text>
      <text class="role" x="245" y="320" text-anchor="middle">Coach</text>

      <text class="contact" x="663" y="228" text-anchor="middle">hallo@seelenraum-beispiel.de</text>
      <text class="contact" x="663" y="290" text-anchor="middle">(0221) 9876-54</text>
      <text class="contact" x="663" y="350" text-anchor="middle">Lindenweg 8, 54321</text>
      <text class="contact" x="663" y="382" text-anchor="middle">Beispielstadt</text>
    </g>
  </svg>

</main>
</body>
</html>
```